Marlow Crate Works Business Cards

WHAT WE DOWe RepairWe CustomizeWe ManufactureWe Deliver
Reason: Hello,
I would like to extend the deadline to May 1st - no additional fee. Reason being is because I am waiting on a reply from feedback from the designed that we are planning on choosing. I would like an answer as soon as possible, please and thanks!!!
Industry/Entity Type
Business
Contact Information for Business Card
Denise Okafor
Vice President
Office: 555-210-4471
Cell: 555-386-9124
Fax: 555-210-4472
denise@marlowcrate.example
Marlow Crate Works II, Inc
2630 Thornbury Road
Fallowmere, IL 60999
www.marlowcrate.example
Look and feel
Each slider illustrates characteristics of the customer's brand and the style your logo design should communicate.

```html
<!DOCTYPE html>
<html lang="en">
<head>
<meta charset="utf-8">
<title>Marlow Crate Works Business Cards</title>
<link href="https://fonts.googleapis.com/css2?family=Questrial&family=Open+Sans:wght@400;600;700&display=swap" rel="stylesheet">
<style>
  :root {
    --brand-red: #f52d0b;
    --ink: #1c1c1c;
    --paper: #ffffff;
    --backdrop: #ecebe8;
    --rule: #8a8a8a;
  }
  * { margin: 0; padding: 0; box-sizing: border-box; }
  html, body { width: 1200px; height: 900px; overflow: hidden; }
  body {
    background: var(--backdrop);
    font-family: "Open Sans", Arial, sans-serif;
    position: relative;
  }
  .card {
    position: absolute;
    width: 540px;
    height: 309px;
    box-shadow: 0 6px 18px rgba(0,0,0,0.18);
  }
  .card--back { left: 40px; top: 296px; background: var(--brand-red); color: var(--paper); }
  .card--front { left: 620px; top: 296px; background: var(--paper); color: var(--ink); }

  /* back side */
  .services { position: absolute; left: 340px; top: 38px; }
  .services__title { font-weight: 700; font-size: 13px; letter-spacing: 0.3px; margin-bottom: 12px; }
  .services__list { list-style: none; padding-left: 14px; }
  .services__list li {
    font-size: 13px; font-weight: 600; line-height: 21px; position: relative; padding-left: 14px;
  }
  .services__list li::before {
    content: ""; position: absolute; left: 0; top: 8px;
    width: 6px; height: 6px; border-radius: 50%; background: var(--paper);
  }
  .wordmark {
    font-family: "Questrial", "Century Gothic", sans-serif;
    text-align: center;
    line-height: 1;
  }
  .card--back .wordmark {
    position: absolute; left: 100px; top: 200px; width: 340px; color: var(--paper);
  }
  .wordmark__main { font-size: 40px; display: block; }
  .wordmark__sub { font-size: 22px; letter-spacing: 1px; display: block; margin-top: 4px; }

  /* front side */
  .contact { position: absolute; left: 318px; top: 36px; font-size: 12px; line-height: 17px; }
  .contact__name { color: var(--brand-red); font-weight: 700; font-size: 15px; line-height: 18px; }
  .contact__role { margin-bottom: 10px; }
  .contact__company { color: var(--brand-red); font-weight: 700; font-size: 13px; }
  .contact__phones { list-style: none; margin-top: 14px; padding-left: 20px; }
  .contact__phones li { display: flex; align-items: center; gap: 8px; font-size: 13px; line-height: 20px; }
  .contact__phones svg { width: 11px; height: 11px; fill: var(--brand-red); }
  .brand-circle {
    position: absolute; left: 106px; top: 118px; width: 70px; height: 70px;
    border-radius: 50%; border: 4px solid var(--ink);
  }
  .card--front .wordmark {
    position: absolute; left: 40px; top: 204px; width: 300px; color: var(--brand-red);
  }
</style>
</head>
<body>

<section class="card card--back" aria-label="Card back">
  <div class="services">
    <h2 class="services__title">WHAT WE DO</h2>
    <ul class="services__list">
      <li>We Repair</li>
      <li>We Customize</li>
      <li>We Manufacture</li>
      <li>We Deliver</li>
    </ul>
  </div>
  <div class="wordmark">
    <span class="wordmark__main">Marlow Crate</span>
    <span class="wordmark__sub">WORKS</span>
  </div>
</section>

<section class="card card--front" aria-label="Card front">
  <div class="contact">
    <div class="contact__name">Denise Okafor</div>
    <div class="contact__role">Vice President</div>
    <div class="contact__company">Marlow Crate Works II, Inc</div>
    <div>2630 Thornbury Road</div>
    <div>Fallowmere, IL 60999</div>
    <ul class="contact__phones">
      <li><svg viewBox="0 0 12 12" aria-hidden="true"><path d="M2.5 0.8l2 2-1 1.4a7 7 0 0 0 4.3 4.3l1.4-1 2 2-1.3 1.7C5.5 11.2 0.8 6.5 0.8 2.1z"/></svg>555-210-4471</li>
      <li><svg viewBox="0 0 12 12" aria-hidden="true"><path d="M3 0h6v12H3zM4 1.5v8h4v-8z"/></svg>555-386-9124</li>
      <li><svg viewBox="0 0 12 12" aria-hidden="true"><path d="M3 0h5v3H3zM1 4h10v7H1zM3 6v1h2V6zm4 0v1h2V6zM3 8v1h2V8zm4 0v1h2V8z"/></svg>555-210-4472</li>
    </ul>
  </div>
  <div class="brand-circle" aria-hidden="true"></div>
  <div class="wordmark">
    <span class="wordmark__main">Marlow Crate</span>
    <span class="wordmark__sub">WORKS</span>
  </div>
</section>

</body>
</html>
```